Masculine Van wrap design for a cleaning company

I would like a design for my property maintenance van. I would like an eye catching and more so masculine design.
Very simple yet modern - think classic plumbing company design but modern
We work in Jersey City across from NYC in condominiums and apartment buildings.
The van is a 2013 Kestro cargo 2500
The color is white - I think gold(burnt yellow) and black will contrast nicely
Went on vacation/holiday
Target Market(s)
apartment building owners
Industry/Entity Type
Cleaning Service
Requirements
Must have
- Drivers side of van (entire length): Logo, Under Logo: Shared Lobby Residence Upkeep
- under Shared Lobby Residence Upkeep: www.BirchKSN.com, under website: (555) 314 - 7260
- Passenger side (same as right): Logo, Under Logo: Shared Lobby Residence Upkeep under S.L.R.U,: www.BirchKSN.com, under website: (555) 314 - 7260
- Servicing Hoboken & Jersey City ( on side anywhere that may fit)
- Back: Right Side door: Logo, under logo: website. Left side door: Shared Lobby Residence Upkeep, under S.L.R.U: 555 314 7260. Under cell phone, Servicing Jersey City & Hoboken
Nice to have
- Colors: black, burnt yellow or burgundy
Should not have
- too much clutter or images. More professional than fun

```html
<!DOCTYPE html>
<html lang="en">
<head>
<meta charset="utf-8">
<title>Birch Kingston Property Maintenance – Van Wrap</title>
<link rel="stylesheet" href="https://fonts.googleapis.com/css2?family=Roboto+Condensed:wght@500;700&display=swap">
<style>
  :root {
    --canvas: #eceef0;
    --body: #ffffff;
    --gold: #c58a1c;
    --burgundy: #5e0f2b;
    --black: #111111;
    --white: #ffffff;
    --outline: #c9ccd1;
  }
  * { margin: 0; padding: 0; box-sizing: border-box; }
  html, body { width: 1200px; height: 800px; overflow: hidden; background: var(--canvas); }
  body { position: relative; font-family: "Roboto Condensed", sans-serif; }

  .panel { position: absolute; overflow: hidden; background: var(--body); border: 1px solid var(--outline); }
  .panel svg.graphics { position: absolute; inset: 0; }
  .text { position: absolute; white-space: nowrap; }

  .brand { display: flex; align-items: center; gap: 16px; }
  .brand-mark { flex: none; background: var(--gold); }
  .brand-name { font-weight: 700; color: var(--gold); text-transform: uppercase; letter-spacing: 1px; }

  /* side panel */
  .side { left: 50px; top: 20px; width: 1100px; height: 470px; border-radius: 40px 14px 14px 70px; }
  .side .brand { left: 440px; top: 110px; }
  .side .brand-name { font-size: 40px; line-height: 46px; }
  .side .brand-mark { width: 26px; height: 26px; }
  .side .tag-front { left: 26px; top: 292px; width: 200px; font-size: 14px; line-height: 20px; font-weight: 500; color: var(--white); text-transform: uppercase; text-align: center; }
  .side .tag-band { left: 330px; top: 306px; font-size: 30px; line-height: 40px; font-weight: 700; color: var(--white); }
  .side .web { left: 300px; top: 356px; font-size: 34px; line-height: 40px; font-weight: 700; color: var(--gold); }
  .side .phone { left: 250px; top: 402px; font-size: 56px; line-height: 60px; font-weight: 700; color: var(--white); }
  .side .area { left: 880px; top: 366px; font-size: 20px; line-height: 26px; font-weight: 500; color: var(--white); }

  /* rear doors */
  .rear { left: 340px; top: 508px; width: 520px; height: 280px; border-radius: 20px 20px 8px 8px; }
  .rear .brand { left: 0; right: 0; top: 28px; justify-content: center; }
  .rear .brand-name { font-size: 24px; line-height: 28px; }
  .rear .brand-mark { width: 18px; height: 18px; }
  .rear .tag { left: 0; right: 0; top: 124px; text-align: center; font-size: 16px; line-height: 22px; font-weight: 700; color: var(--gold); text-transform: uppercase; }
  .rear .web { left: 22px; top: 190px; font-size: 17px; line-height: 22px; font-weight: 500; color: var(--white); }
  .rear .phone { right: 22px; top: 222px; font-size: 32px; line-height: 36px; font-weight: 700; color: var(--white); }
  .rear .area { right: 26px; top: 258px; font-size: 14px; line-height: 18px; font-weight: 500; color: var(--gold); }
</style>
</head>
<body>

<section class="panel side" aria-label="Van side wrap">
  <svg class="graphics" width="1100" height="470" viewBox="0 0 1100 470">
    <defs>
      <linearGradient id="bandFade" x1="0" x2="1">
        <stop offset="0" stop-color="#c58a1c"/>
        <stop offset="0.72" stop-color="#c58a1c"/>
        <stop offset="0.9" stop-color="#111111"/>
      </linearGradient>
    </defs>
    <rect class="band-gold" x="0" y="300" width="1100" height="52" fill="url(#bandFade)"/>
    <path class="front-sweep" d="M0 280 L230 280 L230 352 L0 352 Z" fill="#c58a1c"/>
    <path class="front-burgundy" d="M0 280 Q60 282 90 352 L0 352 Z" fill="#5e0f2b"/>
    <rect class="band-burgundy" x="0" y="352" width="1100" height="118" fill="#5e0f2b"/>
    <line x1="230" y1="40" x2="230" y2="470" stroke="#d8dadd" stroke-width="2"/>
  </svg>
  <div class="text brand"><span class="brand-name">Birch Kingston<br>Property Maintenance</span><span class="brand-mark"></span></div>
  <p class="text tag-front">Shared Lobby Residence<br>Upkeep under S.L.R.U</p>
  <p class="text tag-band">Shared Lobby Residence Upkeep</p>
  <p class="text web">www.BirchKSN.com</p>
  <p class="text phone">(555) 314-7260</p>
  <p class="text area">Servicing<br>Hoboken &amp;<br>Jersey City</p>
</section>

<section class="panel rear" aria-label="Van rear door wrap">
  <svg class="graphics" width="520" height="280" viewBox="0 0 520 280">
    <defs>
      <linearGradient id="rearFade" x1="0" x2="1">
        <stop offset="0" stop-color="#c58a1c"/>
        <stop offset="0.8" stop-color="#c58a1c"/>
        <stop offset="1" stop-color="#111111"/>
      </linearGradient>
    </defs>
    <rect x="0" y="180" width="520" height="42" fill="url(#rearFade)"/>
    <rect x="0" y="222" width="520" height="58" fill="#5e0f2b"/>
    <line x1="260" y1="0" x2="260" y2="280" stroke="#c9ccd1" stroke-width="2"/>
  </svg>
  <div class="text brand"><span class="brand-name">Birch Kingston<br>Property Maintenance</span><span class="brand-mark"></span></div>
  <p class="text tag">Shared Lobby Residence Upkeep<br>under S.L.R.U</p>
  <p class="text web">www.BirchKSN.com</p>
  <p class="text phone">(555) 314-7260</p>
  <p class="text area">Servicing Hoboken &amp; Jersey City</p>
</section>

</body>
</html>
```